Criação de Papelaria Profissional para Marketing & Comunicação
A empresa queria:
" Cursos de oratória particulares, em grupos e in comany; e assessoria de comunicação individual/empresarial. "

```html
<!DOCTYPE html>
<html lang="pt-BR">
<head>
<meta charset="utf-8">
<title>Helena Vasques – Capa e Perfil</title>
<link href="https://fonts.googleapis.com/css2?family=Ubuntu:wght@300;400;500&display=swap" rel="stylesheet">
<style>
  :root {
    --page-bg: #e9ecef;
    --navy: #0b1726;
    --navy-mid: #10263a;
    --circuit-teal: #1f5560;
    --circuit-green: #2d6f5c;
    --circuit-blue: #1b3f63;
    --accent: #7fc3b2;
    --white: #ffffff;
    --muted: #b8c6cf;
    --profile-text: #17324a;
  }
  * { margin: 0; padding: 0; box-sizing: border-box; }
  html, body { width: 1200px; height: 1200px; overflow: hidden; }
  body {
    background: var(--page-bg);
    font-family: "Ubuntu", sans-serif;
    position: relative;
  }
  .profile-card {
    position: absolute;
    left: 40px; top: 440px;
    width: 200px; height: 200px;
    background: var(--white);
    box-shadow: 0 2px 8px rgba(0,0,0,.12);
    display: flex; flex-direction: column; align-items: center; justify-content: center;
    gap: 10px;
  }
  .profile-card .mark-circle {
    width: 38px; height: 38px; border-radius: 50%;
    border: 2px solid var(--accent);
  }
  .profile-card .brand-name {
    font-weight: 500; font-size: 22px; color: var(--profile-text);
  }
  .profile-card .brand-tagline {
    font-weight: 300; font-size: 10px; letter-spacing: 2px; color: var(--accent);
    margin-top: -6px;
  }
  .cover {
    position: absolute;
    left: 260px; top: 430px;
    width: 900px; height: 370px;
    background: var(--navy);
    overflow: hidden;
  }
  .cover-photo {
    position: absolute; right: 0; top: 0;
    width: 62%; height: 100%;
    background:
      radial-gradient(circle at 75% 40%, var(--circuit-green) 0%, transparent 45%),
      radial-gradient(circle at 55% 75%, var(--circuit-blue) 0%, transparent 50%),
      linear-gradient(135deg, var(--circuit-teal), var(--navy-mid));
  }
  .cover-photo::after {
    content: ""; position: absolute; inset: 0;
    background: linear-gradient(90deg, var(--navy) 0%, rgba(11,23,38,.55) 35%, rgba(11,23,38,0) 70%);
  }
  .cover-identity {
    position: absolute; left: 395px; top: 70px;
    width: 360px; text-align: center;
  }
  .cover-identity .mark-circle {
    width: 56px; height: 56px; border-radius: 50%;
    border: 2px solid var(--accent); margin: 0 auto 14px;
  }
  .cover-identity .brand-name {
    color: var(--white); font-weight: 500; font-size: 50px; line-height: 1;
  }
  .cover-identity .brand-tagline {
    color: var(--accent); font-weight: 300; font-size: 24px; letter-spacing: 3px;
    margin-top: 8px;
  }
  .contact-row {
    position: absolute; left: 330px; bottom: 34px;
    display: flex; gap: 34px; align-items: center;
  }
  .contact-item { display: flex; align-items: center; gap: 10px; }
  .contact-icon {
    width: 24px; height: 24px; background: var(--muted); border-radius: 3px;
    display: flex; align-items: center; justify-content: center;
  }
  .contact-text {
    color: var(--muted); font-size: 9.5px; line-height: 1.45; font-weight: 400;
  }
</style>
</head>
<body>
  <div class="profile-card">
    <div class="mark-circle"></div>
    <div class="brand-name">Helena Vasques</div>
    <div class="brand-tagline">Comunicação e Oratória</div>
  </div>

  <section class="cover">
    <div class="cover-photo" role="img" aria-label="Fotografia em close de uma placa de circuito em tons de verde-azulado"></div>

    <div class="cover-identity">
      <div class="mark-circle"></div>
      <div class="brand-name">Helena Vasques</div>
      <div class="brand-tagline">Comunicação e Oratória</div>
    </div>

    <div class="contact-row">
      <div class="contact-item">
        <span class="contact-icon">
          <svg width="14" height="14" viewBox="0 0 24 24"><path fill="#0b1726" d="M6.6 10.8a15 15 0 0 0 6.6 6.6l2.2-2.2c.3-.3.7-.4 1-.2 1.1.4 2.3.6 3.6.6.6 0 1 .4 1 1V20c0 .6-.4 1-1 1A17 17 0 0 1 3 4c0-.6.4-1 1-1h3.5c.6 0 1 .4 1 1 0 1.2.2 2.4.6 3.6.1.3 0 .7-.2 1z"/></svg>
        </span>
        <span class="contact-text">(31) 94410-2256<br>(31) 97720-1183</span>
      </div>
      <div class="contact-item">
        <span class="contact-icon">
          <svg width="14" height="14" viewBox="0 0 24 24"><path fill="#0b1726" d="M12 2a7 7 0 0 0-7 7c0 5 7 13 7 13s7-8 7-13a7 7 0 0 0-7-7zm0 9.5A2.5 2.5 0 1 1 12 6.5a2.5 2.5 0 0 1 0 5z"/></svg>
        </span>
        <span class="contact-text">Rua das Acácias, Nº 148 - Centro<br>Cidade/UF CEP 30140-200</span>
      </div>
      <div class="contact-item">
        <span class="contact-icon">
          <svg width="14" height="14" viewBox="0 0 24 24"><path fill="#0b1726" d="M3 5h18v14H3zm2 2v.5l7 4.5 7-4.5V7l-7 4.5z"/></svg>
        </span>
        <span class="contact-text">contato@helenavasques.com.br<br>www.helenavasques.com.br</span>
      </div>
    </div>
  </section>
</body>
</html>
```